Bright Fern Series- Face & Body Oil Label

Hi,
I need a label design for a new brand- "Bright Fern Series". Modern and expensive looking. Any color scheme. Feel free to be creative! (I'm not set on the brand name above... I was also thinking maybe "TIRA" or "PuraLume".
-Packaging: 4oz / 118mL clear glass "boston round" bottle with a white treatment pump. The product is an oil so it has a golden tint.
-Product: 4oz Biotin & Marula Face & Body Oil (note that the featured ingredients will change. Others will be "Rosehip & Vitamin E", "Lavender & Hemp Seed Oil", "Coconut Oil & Vitamin C"
-Label size: 5" x 2.5" rounded corners
-Main Highlight: "Moisturizing & Healing"
-Other Highlights:
-----non-greasy
-----all-natural
-----paraben-free
-----vegan
(feel free to use icon symbols)
-Ingredient deck attached
-Other info:
----made in Los Angeles, CA
----manufactured by Willowmere Labs LLC
----UPC
The main thing here is the logo and textures to the label. I can fill in / rearrange the info after.
Thank you,
Owen

```html
<!DOCTYPE html>
<html lang="en">
<head>
<meta charset="utf-8">
<title>Bright Fern Series – Vitamin E Face &amp; Body Oil Label</title>
<link href="https://fonts.googleapis.com/css2?family=Oswald:wght@600&family=Montserrat:wght@400;500;600;700&display=swap" rel="stylesheet">
<style>
  :root {
    --page: #eef0ef;
    --label: #ffffff;
    --ink: #2b2d33;
    --teal: #3aa79a;
    --teal-soft: #8fd0c6;
    --teal-faint: #e2f2ef;
    --tan: #cdb092;
  }
  * { margin: 0; padding: 0; box-sizing: border-box; }
  html, body {
    width: 1200px; height: 1200px; overflow: hidden;
    background: var(--page);
  }
  .canvas { position: relative; width: 1200px; height: 1200px; }
  .label {
    position: absolute; left: 220px; top: 115px;
    width: 760px; height: 970px;
    background: var(--label);
    border-radius: 28px;
    overflow: hidden;
    box-shadow: 0 4px 18px rgba(0,0,0,0.06);
    font-family: "Montserrat", sans-serif;
  }
  .rule {
    position: absolute; top: 104px; height: 8px; background: var(--tan);
  }
  .rule--left { left: 0; width: 190px; }
  .rule--right { right: 0; width: 215px; }
  .brand {
    position: absolute; left: 210px; top: 76px; width: 330px;
    display: flex; align-items: center; gap: 12px;
  }
  .brand-dot {
    width: 26px; height: 26px; border-radius: 50%; background: var(--ink); flex: none;
  }
  .brand-name {
    font-weight: 700; color: var(--ink); text-transform: uppercase;
    font-size: 24px; line-height: 1.05; letter-spacing: 0.5px;
  }
  .foliage-faint {
    position: absolute; left: 250px; top: 640px; width: 330px; height: 330px;
    border-radius: 50% 50% 0 50%;
    background: radial-gradient(circle at 50% 50%, var(--teal-faint), rgba(226,242,239,0.3));
  }
  .foliage {
    position: absolute; left: 0; top: 730px; width: 270px; height: 240px;
    border-radius: 0 100% 0 0;
    background: linear-gradient(135deg, var(--teal-soft), var(--teal));
  }
  .title {
    position: absolute; left: 0; right: 0; top: 352px; text-align: center;
    font-family: "Oswald", sans-serif; font-weight: 600;
    font-size: 122px; line-height: 1; color: var(--ink); letter-spacing: 1px;
  }
  .subtitle {
    position: absolute; left: 0; right: 0; top: 510px; text-align: center;
    font-weight: 400; font-size: 46px; color: var(--teal); letter-spacing: 1px;
  }
  .claim {
    position: absolute; left: 0; right: 0; top: 604px; text-align: center;
    font-weight: 600; font-size: 28px; color: var(--ink); letter-spacing: 0.5px;
  }
  .highlight {
    position: absolute; left: 144px; width: 480px; top: 677px; height: 58px;
    background: var(--teal); color: #fff;
    display: flex; align-items: center; justify-content: center;
    font-weight: 500; font-size: 28px; letter-spacing: 1px;
  }
  .features {
    position: absolute; left: 0; right: 0; top: 770px; text-align: center;
    font-weight: 400; font-size: 29px; color: var(--teal); letter-spacing: 0.5px;
  }
  .volume {
    position: absolute; left: 0; right: 0; top: 902px; text-align: center;
    font-weight: 500; font-size: 24px; color: var(--ink); letter-spacing: 1px;
  }
  .badge {
    position: absolute; left: 640px; width: 90px; text-align: center;
  }
  .badge svg { display: block; margin: 0 auto; }
  .badge-text {
    margin-top: 8px; font-size: 15px; font-weight: 600; color: var(--ink);
    letter-spacing: 0.5px; white-space: nowrap;
  }
  .badge--vegan { top: 672px; }
  .badge--natural { top: 816px; }
</style>
</head>
<body>
<div class="canvas">
  <div class="label">
    <div class="rule rule--left"></div>
    <div class="rule rule--right"></div>
    <div class="brand">
      <span class="brand-dot"></span>
      <span class="brand-name">Bright Fern<br>Series</span>
    </div>

    <div class="foliage-faint" role="img" aria-label="Faint large tropical leaf illustration behind the text"></div>
    <div class="foliage" role="img" aria-label="Teal tropical leaf illustration in the lower left corner"></div>

    <h1 class="title">VITAMIN E</h1>
    <p class="subtitle">FACE &amp; BODY OIL</p>
    <p class="claim">100% NATURAL</p>
    <div class="highlight">HYDRATE &amp; BALANCE</div>
    <p class="features">NON-GREASY | PARABEN-FREE</p>
    <p class="volume">4OZ / 118ML</p>

    <div class="badge badge--vegan">
      <svg width="76" height="76" viewBox="0 0 76 76"><circle cx="38" cy="38" r="35" fill="none" stroke="#2b2d33" stroke-width="2"/></svg>
      <div class="badge-text">VEGAN</div>
    </div>
    <div class="badge badge--natural">
      <svg width="76" height="76" viewBox="0 0 76 76"><circle cx="38" cy="38" r="35" fill="none" stroke="#2b2d33" stroke-width="2"/></svg>
      <div class="badge-text">ALL-NATURAL</div>
    </div>
  </div>
</div>
</body>
</html>
```